RVT Business Card Design

We are an independent auto dealer who specializes in commercial & fleet vehicles, we are family owned and operated and have been in business since 2001. We stock late model, low mileage, white trucks & vans. We mostly deal with companies in the construction and service industries. We are just looking to try to freshen up our old business card, we do not want to change the logo at this point, because it is well know within the southwest region & construction community. I have attached our logo and a PDF of our current business card for reference.
Updates
If the address is stacked there is no comma (,) after NE. Everyone keeps putting it in with this format and it is not correct.
482 Montrose Ave NE
Albuquerque, NM 87193
If the address is all on one line, then there will be a comma (,) after NE
482 Montrose Ave NE, Albuquerque, NM 87193
Please make changes accordingly, thank you for your attention in this matter.
Industry/Entity Type
Construction
Contact Information for Business Card
482 Montrose Ave NE, Albuquerque, NM 87193, Dorian Wexhall, Vice President, dorian@rvtfleetmotors.com, www.RVTfleetmotors.com, ph 505-271-6048, fax 505-617-2094, cell 505-438-7720

```html
<!DOCTYPE html>
<html lang="en">
<head>
<meta charset="utf-8">
<title>RVT Auto Sales – Business Card</title>
<link href="https://fonts.googleapis.com/css2?family=Open+Sans:wght@400;600;700&display=swap" rel="stylesheet">
<style>
  :root {
    --backdrop: #b9b9b9;
    --card-white: #ffffff;
    --card-black: #050505;
    --brand-red: #e3202a;
    --ink: #111111;
    --paper-text: #ffffff;
  }
  * { margin: 0; padding: 0; box-sizing: border-box; }
  html, body {
    width: 1200px; height: 688px; overflow: hidden;
    background: var(--backdrop);
    font-family: "Open Sans", Arial, sans-serif;
  }
  .card {
    position: absolute; left: 183px; top: 108px;
    width: 834px; height: 473px;
    background: var(--card-white);
    overflow: hidden;
  }
  .brand-name {
    position: absolute; left: 30px; top: 118px;
    font-size: 62px; font-weight: 700; line-height: 1;
    color: var(--ink); letter-spacing: -0.5px;
  }
  .person {
    position: absolute; right: 33px; top: 88px; text-align: right;
  }
  .person-name {
    font-size: 30px; font-weight: 700; color: var(--brand-red); line-height: 1.2;
  }
  .person-title {
    font-size: 20px; font-weight: 400; color: var(--ink); margin-top: 6px;
  }
  .contact-band {
    position: absolute; left: 0; top: 250px; width: 100%; height: 223px;
    background: var(--card-black);
  }
  .stripe {
    position: absolute; left: 0; width: 100%; height: 4px;
    background: var(--brand-red);
  }
  .stripe-upper { top: 10px; }
  .stripe-lower { top: 23px; }
  .contact-list {
    position: absolute; left: 38px; top: 63px; list-style: none;
  }
  .contact-item {
    display: flex; align-items: center; height: 33.5px;
    font-size: 20px; color: var(--paper-text);
  }
  .contact-icon {
    width: 22px; height: 22px; margin-right: 14px; flex: none;
  }
  .company-address {
    position: absolute; right: 33px; top: 62px; text-align: right;
    font-style: normal; font-size: 20px; color: var(--paper-text);
    line-height: 33.5px;
  }
  .company-name { color: var(--brand-red); font-weight: 700; }
</style>
</head>
<body>
  <main class="card">
    <div class="brand-name">RVT Auto Sales</div>

    <div class="person">
      <div class="person-name">Dorian Wexhall</div>
      <div class="person-title">Vice President</div>
    </div>

    <section class="contact-band">
      <div class="stripe stripe-upper"></div>
      <div class="stripe stripe-lower"></div>

      <ul class="contact-list">
        <li class="contact-item">
          <svg class="contact-icon" viewBox="0 0 22 22" aria-label="Phone">
            <rect width="22" height="22" rx="3" fill="var(--brand-red)"/>
            <path d="M6.5 4.5l3 3-1.6 1.8c.9 1.9 2.3 3.3 4.2 4.2l1.8-1.6 3 3-1.8 2c-5.2-.6-9.5-4.9-10.1-10.1z" fill="var(--card-black)"/>
          </svg>
          505-271-6048
        </li>
        <li class="contact-item">
          <svg class="contact-icon" viewBox="0 0 22 22" aria-label="Fax">
            <rect width="22" height="22" rx="3" fill="var(--brand-red)"/>
            <rect x="7" y="4" width="8" height="5" fill="var(--card-black)"/>
            <rect x="4" y="9" width="14" height="7" rx="1" fill="var(--card-black)"/>
            <rect x="7" y="13" width="8" height="5" fill="var(--card-black)" stroke="var(--brand-red)" stroke-width="1"/>
          </svg>
          505-617-2094
        </li>
        <li class="contact-item">
          <svg class="contact-icon" viewBox="0 0 22 22" aria-label="Mobile">
            <rect width="22" height="22" rx="3" fill="var(--brand-red)"/>
            <rect x="7" y="3.5" width="8" height="15" rx="1.5" fill="var(--card-black)"/>
            <rect x="8.3" y="5.5" width="5.4" height="9" fill="var(--brand-red)"/>
            <circle cx="11" cy="16.5" r="0.9" fill="var(--brand-red)"/>
          </svg>
          505-438-7720
        </li>
        <li class="contact-item">
          <svg class="contact-icon" viewBox="0 0 22 22" aria-label="Email">
            <rect width="22" height="22" rx="3" fill="var(--brand-red)"/>
            <rect x="4" y="6" width="14" height="10" fill="var(--card-black)"/>
            <path d="M4.5 6.5l6.5 5 6.5-5" fill="none" stroke="var(--brand-red)" stroke-width="1.3"/>
          </svg>
          dorian@rvtfleetmotors.com
        </li>
      </ul>

      <address class="company-address">
        <div class="company-name">RVT Auto Sales</div>
        <div>482 Montrose Ave NE</div>
        <div>Albuquerque, NM 87193</div>
        <div>www.RVTfleetmotors.com</div>
      </address>
    </section>
  </main>
</body>
</html>
```